*YO!!! Designers Needed!!* Front Page Cover Needed for a $$Billion Dollar$$ Company

We are a manufacturer of aluminum electrolytic capacitors. We are looking to create a front page cover that will be used on our annual report. We are a publicly listed company and work with many Brellmont 500 companies, so your work will be viewed by the BIG GUNS and EXECUTIVES around the WORLD! If selected, you may be selected for additional work.

The front page cover should be unique. If elegance, modern, bling, and creativity somehow got together and had a child, that's what the cover page would look like!

Inspired Examples attached. Check them out!

www.kovantro.com

Font styles to use
Sans Serif

Requirements
Must have
• 1. Must include the attached logo. Logo size, color, and placement are at your discretion.

2. Should include the text, '2020 Annual Report'

3. The design should incorporate the use of foil and/or be embossed. The foil can be part of the design or can be the full page. See various examples attached for reference.

4. Shall be in A4 size and vertical orientation.
Nice to have
• Feel free to add any icons or stock photos (for example capacitors or circuit boards) if needed.

Be creative here and don't be afraid to be bold! The end product will be printed and budget is not a limiting factor, so feel free to make it extravagant if needed.

Our slogan is "Think Ahead". This slogan can or cannot be part of the theme.

```html
<!DOCTYPE html>
<html lang="en">
<head>
<meta charset="utf-8">
<title>Kovantro — 2020 Annual Report Cover</title>
<link rel="stylesheet" href="https://fonts.googleapis.com/css2?family=Jost:wght@400;600&display=swap">
<style>
  :root {
    --stage: #17110b;
    --cover-black: #0b0b0c;
    --cover-swirl: #1d1d20;
    --cover-swirl-soft: #161618;
    --gold-light: #e8cf86;
    --gold-mid: #c9a551;
    --gold-deep: #9a7430;
    --ink: #141414;
  }
  * { margin: 0; padding: 0; box-sizing: border-box; }
  html, body {
    width: 1200px;
    height: 789px;
    overflow: hidden;
    background: var(--stage);
  }
  .canvas {
    position: relative;
    width: 1200px;
    height: 789px;
    display: flex;
    align-items: center;
    justify-content: center;
  }
  .cover {
    position: relative;
    width: 523px;
    height: 740px;
    background: var(--cover-black);
    box-shadow: 0 10px 40px rgba(0, 0, 0, 0.6);
    overflow: hidden;
  }
  .cover__pattern {
    position: absolute;
    inset: 0;
    background:
      radial-gradient(ellipse 60% 22% at 30% 12%, var(--cover-swirl) 0%, transparent 100%),
      radial-gradient(ellipse 55% 20% at 75% 30%, var(--cover-swirl-soft) 0%, transparent 100%),
      radial-gradient(ellipse 65% 24% at 25% 58%, var(--cover-swirl) 0%, transparent 100%),
      radial-gradient(ellipse 60% 22% at 72% 72%, var(--cover-swirl) 0%, transparent 100%),
      radial-gradient(ellipse 70% 22% at 35% 90%, var(--cover-swirl-soft) 0%, transparent 100%),
      linear-gradient(160deg, #121214 0%, var(--cover-black) 50%, #131315 100%);
  }
  .cover__frame {
    position: absolute;
    left: 186px;
    top: 210px;
    width: 178px;
    height: 178px;
    border: 1.5px solid var(--gold-deep);
  }
  .cover__foil {
    position: absolute;
    left: 70px;
    top: 252px;
    width: 392px;
    height: 92px;
    border-radius: 4px 10px 6px 12px;
    background: linear-gradient(100deg, var(--gold-deep) 0%, var(--gold-mid) 16%, var(--gold-light) 46%, var(--gold-mid) 78%, var(--gold-deep) 100%);
  }
  .cover__brand {
    position: absolute;
    left: 186px;
    width: 178px;
    top: 274px;
    text-align: center;
    font-family: "Jost", sans-serif;
    font-weight: 600;
    font-size: 42px;
    color: var(--ink);
    line-height: 1;
  }
  .cover__title {
    position: absolute;
    left: 96px;
    top: 408px;
    font-family: "Jost", sans-serif;
    font-weight: 400;
    font-size: 15px;
    letter-spacing: 8px;
    color: var(--gold-mid);
    text-transform: uppercase;
    white-space: nowrap;
  }
</style>
</head>
<body>
  <main class="canvas">
    <section class="cover">
      <div class="cover__pattern" role="img" aria-label="Embossed black-on-black flowing swirl pattern covering the whole cover"></div>
      <div class="cover__frame"></div>
      <div class="cover__foil" role="img" aria-label="Gold foil brush stroke behind the company name"></div>
      <div class="cover__brand">Kovantro</div>
      <h1 class="cover__title">2020 Annual Report</h1>
    </section>
  </main>
</body>
</html>
```